Halvers Produce Business Cards

A new style and great looking business cards for my parents business. Simple yet catchy and something that shows a home grown produce and apples farm!

Target Market(s)

Farmers market buyers, someone who loves home grown produce, fresh vegetables and apples.

Industry/Entity Type

Business

Requirements
Must have
• Halvers Produce is the name, so that will have to be on the card. Also incorporate our logo! but maybe not exactly the same? Open to all ideas!

Leocadia Farnes ( Owner)

Address: 47 Oak Crest Dr.
Alder Falls, OR 98437

Phone: (541) 555-0147
Cell (541) 555-0182
Nice to have
• I have a logo that was done not too long ago using design! I would like to have parts of the logo be used, but I also want examples of NOT using the logo and see if we can get the family produce look too it!

```html
<!DOCTYPE html>
<html lang="en">
<head>
<meta charset="utf-8">
<title>Halvers Produce Business Cards</title>
<link rel="stylesheet" href="https://fonts.googleapis.com/css2?family=Jost:wght@400;700&display=swap">
<style>
  :root {
    --page-bg: #ece9e4;
    --card-white: #ffffff;
    --ink: #1d1d1f;
    --accent-green: #1f9a45;
    --deep-green: #0a6e35;
    --mid-green: #0e8a3e;
    --leaf-green: #8cc63f;
    --lime: #d6e021;
    --badge-blue: #1d5f82;
    --faint-art: #e6e6e6;
  }
  * { box-sizing: border-box; margin: 0; padding: 0; }
  html, body { width: 1200px; height: 900px; overflow: hidden; }
  body {
    background: var(--page-bg);
    font-family: "Jost", sans-serif;
    color: var(--ink);
    position: relative;
  }
  .card {
    position: absolute;
    top: 275px;
    width: 560px;
    height: 320px;
    border-radius: 14px;
    overflow: hidden;
    box-shadow: 0 4px 14px rgba(0,0,0,0.18);
  }
  .card-front { left: 28px; background: var(--card-white); border: 1px solid #333; }
  .card-back {
    left: 614px;
    background: radial-gradient(ellipse at 50% 30%, var(--mid-green) 0%, var(--deep-green) 80%);
  }
  .side-bar {
    position: absolute; left: 0; top: 96px;
    width: 9px; height: 142px;
    background: var(--accent-green);
  }
  .contact { position: absolute; left: 50px; top: 92px; font-size: 15px; line-height: 1.28; }
  .contact-name { font-weight: 700; font-size: 17px; }
  .contact-role { font-size: 12.5px; margin-bottom: 16px; }
  .contact-block { margin-bottom: 16px; }
  .field-art {
    position: absolute; left: 140px; bottom: 0;
    width: 420px; height: 160px;
    background: radial-gradient(ellipse at 70% 80%, var(--faint-art) 0%, rgba(230,230,230,0.4) 50%, rgba(255,255,255,0) 75%);
  }
  .brand-badge {
    position: absolute;
    display: flex; align-items: center; justify-content: center;
    border-radius: 50%;
    background: var(--card-white);
    text-align: center;
  }
  .brand-badge-front {
    left: 330px; top: 68px; width: 180px; height: 180px;
    border: 6px solid var(--badge-blue);
  }
  .brand-badge-back {
    left: 180px; top: 40px; width: 200px; height: 200px;
    border: 6px solid var(--badge-blue);
    box-shadow: 0 3px 10px rgba(0,0,0,0.25);
  }
  .brand-name {
    font-weight: 700; color: var(--accent-green);
    font-size: 27px; line-height: 1.05;
  }
  .brand-badge-back .brand-name { font-size: 30px; }
  .field-band {
    position: absolute; left: 0; bottom: 0;
    width: 560px; height: 90px;
    background: linear-gradient(180deg, rgba(31,154,69,0) 0%, var(--accent-green) 30%, var(--leaf-green) 70%, var(--lime) 100%);
  }
</style>
</head>
<body>
  <section class="card card-front" aria-label="Business card front">
    <div class="field-art" role="img" aria-label="Faint farm scene with sun over fields"></div>
    <div class="side-bar"></div>
    <div class="contact">
      <div class="contact-name">Leocadia Farnes</div>
      <div class="contact-role">Owner</div>
      <div class="contact-block">Address: 47 Oak Crest Dr.<br>Alder Falls, OR 98437</div>
      <div>Phone: (541) 555-0147<br>Cell (541) 555-0182</div>
    </div>
    <div class="brand-badge brand-badge-front">
      <span class="brand-name">Halvers<br>Produce</span>
    </div>
  </section>

  <section class="card card-back" aria-label="Business card back">
    <div class="brand-badge brand-badge-back">
      <span class="brand-name">Halvers<br>Produce</span>
    </div>
    <div class="field-band" role="img" aria-label="Green and lime rolling field decoration"></div>
  </section>
</body>
</html>
```